Book Cover Design Project

Cover design using photo provided.
Title is as follows:-

Harold Edmund Tessler

"Marching beside the Quiet Harbour"

By Dennis Palgrave

Just Added Picture and extended design a further 7 days

```html
<!DOCTYPE html>
<html lang="en">
<head>
<meta charset="utf-8">
<title>Harold Edmund Tessler — Marching beside the Quiet Harbour</title>
<link rel="stylesheet" href="https://fonts.googleapis.com/css2?family=Cinzel:wght@700&family=Zilla+Slab:wght@500&family=League+Gothic&family=Archivo+Black&display=swap">
<style>
  :root {
    --sky-dark: #1b2029;
    --sky-mid: #4a525e;
    --sky-light: #8a929c;
    --navy: #1c3c7c;
    --title-red: #7b1a0f;
    --silver: #e4e4e4;
    --white: #ffffff;
    --sepia-light: #e8dcc0;
    --sepia-dark: #6b5a3e;
  }
  * { margin: 0; padding: 0; box-sizing: border-box; }
  html, body { width: 792px; height: 1200px; overflow: hidden; background: var(--sky-dark); }
  .cover {
    position: relative;
    width: 792px;
    height: 1200px;
    overflow: hidden;
  }
  .aerial-backdrop {
    position: absolute;
    inset: 0;
    background:
      radial-gradient(ellipse at 70% 75%, rgba(200,205,212,0.35), transparent 60%),
      radial-gradient(ellipse at 20% 60%, rgba(150,158,168,0.3), transparent 55%),
      linear-gradient(180deg, var(--sky-dark) 0%, var(--sky-mid) 45%, var(--sky-light) 100%);
  }
  .type-layer {
    position: absolute;
    inset: 0;
  }
  .portrait {
    position: absolute;
    left: 164px;
    top: 376px;
    width: 484px;
    height: 551px;
    background: var(--white);
    padding: 13px;
    transform: rotate(-14deg);
    box-shadow: 0 8px 22px rgba(0,0,0,0.55);
  }
  .portrait-photo {
    width: 100%;
    height: 100%;
    background:
      radial-gradient(ellipse at 50% 62%, #1f2a2a 0%, #2a3030 35%, transparent 60%),
      linear-gradient(100deg, var(--sepia-dark) 0%, var(--sepia-light) 30%, #d9cba8 70%, #a89470 100%);
  }
  .series-name {
    font-family: "Cinzel", "Times New Roman", serif;
    font-weight: 700;
    fill: var(--navy);
    stroke: var(--white);
    stroke-width: 3px;
    paint-order: stroke fill;
  }
  .subtitle-lead {
    font-family: "Zilla Slab", "Rockwell", serif;
    font-weight: 500;
    fill: var(--silver);
  }
  .subtitle-main {
    font-family: "League Gothic", "Impact", sans-serif;
    fill: var(--title-red);
    stroke: var(--white);
    stroke-width: 4px;
    paint-order: stroke fill;
  }
  .author-line {
    font-family: "Archivo Black", "Arial Black", sans-serif;
    fill: var(--navy);
    stroke: var(--white);
    stroke-width: 4px;
    paint-order: stroke fill;
  }
</style>
</head>
<body>
<main class="cover">
  <div class="aerial-backdrop" role="img" aria-label="Aerial black-and-white photograph of a city with a winding river and drifting clouds"></div>

  <figure class="portrait">
    <div class="portrait-photo" role="img" aria-label="Hand-tinted studio portrait of an airman in dark uniform and side cap"></div>
  </figure>

  <svg class="type-layer" width="792" height="1200" viewBox="0 0 792 1200" aria-label="Cover title">
    <text class="series-name" x="396" y="108" text-anchor="middle" font-size="58" textLength="712" lengthAdjust="spacingAndGlyphs">HAROLD EDMUND TESSLER</text>
    <text class="subtitle-lead" x="398" y="184" text-anchor="middle" font-size="46" textLength="540" lengthAdjust="spacingAndGlyphs">Marching beside the</text>
    <text class="subtitle-main" x="418" y="398" text-anchor="middle" font-size="262" textLength="664" lengthAdjust="spacingAndGlyphs">QUIET HARBOUR</text>
    <text class="author-line" x="398" y="1098" text-anchor="middle" font-size="58" textLength="610" lengthAdjust="spacingAndGlyphs">By Dennis Palgrave</text>
  </svg>
</main>
</body>
</html>
```